herbal supplement label

This is the label for bottle. Our brand name is Vel'dora, which stands for "natural nutrition." We would like to a label that implies the meaning of our brand. A feeling of natural, organic, healthy, trustworthy and scientific. Basically, we want a rurally fresh feeling with some modern styles. I provide labels in the attachment.

Project Deadline Extended
Reason: I want to have further communication with designers and wait for some more good design.

Industry/Entity Type

Nutrition

```html
<!DOCTYPE html>
<html lang="en">
<head>
<meta charset="utf-8">
<title>Vel'dora Herbal Supplement Labels</title>
<link href="https://fonts.googleapis.com/css2?family=Nunito:wght@300;400;800&family=Arimo:wght@400;700&display=swap" rel="stylesheet">
<style>
  :root {
    --paper: #e9e6de;
    --paper-light: #f1efe9;
    --fold: rgba(120,110,95,0.18);
    --ink: #4a4a4a;
    --ink-soft: #6d6d6d;
    --white: #ffffff;
    --green: #7cd220;
    --green-dark: #6bbf17;
    --orange: #f07d38;
    --orange-dark: #e46d27;
    --purple: #9347e8;
    --purple-dark: #8237d9;
    --teal: #2e9ea6;
    --magenta: #d1397c;
    --blue: #3a5fb6;
    --sub: #7fa8ab;
  }
  * { box-sizing: border-box; margin: 0; padding: 0; }
  html, body { width: 927px; height: 1200px; overflow: hidden; background: #fff; }
  body { position: relative; font-family: "Arimo", Arial, sans-serif; color: var(--ink); }

  .label { position: absolute; left: 65px; width: 800px; height: 345px; background: var(--paper); overflow: hidden; }
  .label--heart { top: 33px; --accent: var(--green); --accent-dark: var(--green-dark); --title: var(--teal); --tint: rgba(124,210,32,0.18); }
  .label--energy { top: 412px; --accent: var(--orange); --accent-dark: var(--orange-dark); --title: var(--magenta); --tint: rgba(240,125,56,0.15); }
  .label--nose { top: 791px; --accent: var(--purple); --accent-dark: var(--purple-dark); --title: var(--blue); --tint: rgba(147,71,232,0.12); }

  .panel { position: absolute; top: 0; height: 345px; }
  .panel--left { left: 0; width: 216px; }
  .panel--center { left: 216px; width: 332px; background: var(--paper-light); box-shadow: inset 3px 0 4px var(--fold), inset -3px 0 4px var(--fold); }
  .panel--right { left: 548px; width: 252px; }

  .band-top { position: absolute; left: 0; top: 0; width: 100%; height: 85px; background: var(--accent-dark); }
  .panel--center .band-top { height: 100px; background: var(--accent); }
  .band-bottom { position: absolute; left: 0; bottom: 0; width: 100%; height: 27px; background: var(--accent-dark); }
  .panel--center .band-bottom { height: 31px; background: var(--accent); }
  .dash { position: absolute; left: 10px; right: 10px; border-top: 1px dashed rgba(255,255,255,0.8); }
  .dash--top { top: 78px; }
  .dash--bottom { bottom: 8px; }

  .brand-top { position: absolute; top: 28px; width: 100%; text-align: center; font-family: "Nunito", sans-serif; font-weight: 400; font-size: 23px; color: var(--white); letter-spacing: 0.5px; }

  .product-name { position: absolute; top: 160px; width: 100%; text-align: center; font-family: "Nunito", sans-serif; font-weight: 800; font-size: 31px; line-height: 1; color: var(--title); }
  .product-type { position: absolute; top: 197px; width: 100%; text-align: center; font-family: "Nunito", sans-serif; font-weight: 300; font-size: 19px; color: var(--sub); letter-spacing: 0.3px; }
  .count { position: absolute; top: 290px; right: 32px; font-family: "Arimo", sans-serif; font-weight: 700; font-size: 13px; color: var(--title); }

  .notes { position: absolute; left: 14px; top: 92px; width: 192px; font-size: 7.2px; line-height: 8.6px; color: var(--ink-soft); }
  .notes strong { font-weight: 700; text-transform: uppercase; color: var(--ink); }
  .notes .fda { background: var(--tint); display: block; margin: 1px 0; }
  .brand-side { position: absolute; left: 0; width: 216px; top: 274px; text-align: center; font-family: "Nunito", sans-serif; font-weight: 800; font-size: 20px; color: var(--green-dark); }
  .web { position: absolute; left: 0; width: 216px; top: 302px; text-align: center; font-size: 8px; color: var(--ink-soft); }

  .usage { position: absolute; left: 8px; top: 96px; width: 240px; font-size: 7.4px; line-height: 9px; color: var(--ink); }
  .usage strong { font-weight: 700; text-transform: uppercase; }
  .facts { position: absolute; left: 14px; top: 124px; width: 226px; height: 128px; border: 1px dashed rgba(110,110,110,0.55); padding: 6px 8px; background: rgba(255,255,255,0.35); font-size: 7.6px; line-height: 10px; color: var(--ink); }
  .facts h3 { font-family: "Arimo", sans-serif; font-weight: 400; font-size: 14px; line-height: 18px; color: var(--ink); }
  .facts .rule { border-top: 1px dashed rgba(110,110,110,0.55); margin: 2px 0; }
  .facts .row { display: flex; justify-content: space-between; }
  .facts .head { font-size: 6.4px; }
  .facts .caps { text-transform: uppercase; }
  .facts .foot { font-size: 6.4px; margin-top: 3px; }
</style>
</head>
<body>

<section class="label label--heart">
  <div class="panel panel--left">
    <div class="band-top"><div class="dash dash--top"></div></div>
    <p class="notes"><strong>Contains:</strong> All natural herbs and fibers. No sugar, salt, corn, soy, yeast, wheat, milk or preservatives.<br><strong>Caution:</strong><br>Pregnant women, children and anyone with disease should consult with their medical doctor prior to taking this product.<br><strong>Store in a cool, dry place below 30°C.</strong><br><strong>Avoid direct sunlight.</strong><br><strong>Keep out of reach of children.</strong><span class="fda">This statement has not been evaluated by the Food and Drug Administration. This product is not intended to diagnose, treat, cure or prevent any disease.</span><strong>Manufactured by:</strong><br>Ridgeway Herbal Labs Inc<br>Fairbrook, CA 90210</p>
    <div class="brand-side">Vel'dora</div>
    <div class="web">www.veldoranatural.com</div>
    <div class="band-bottom"><div class="dash dash--bottom"></div></div>
  </div>
  <div class="panel panel--center">
    <div class="band-top"></div>
    <div class="brand-top">Vel'dora</div>
    <h2 class="product-name">Cardio Calm</h2>
    <p class="product-type">Dietary Supplement</p>
    <p class="count">90 Capsules</p>
    <div class="band-bottom"></div>
  </div>
  <div class="panel panel--right">
    <div class="band-top"><div class="dash dash--top"></div></div>
    <p class="usage"><strong>Suggested use:</strong><br>Take 2 to 3 capsules twice a day or as directed by healthcare professional.</p>
    <div class="facts">
      <h3>Supplement Facts</h3>
      <div class="rule"></div>
      <div>Serving Size: 2 Capsule</div>
      <div>Serving Per Container: 45</div>
      <div class="rule"></div>
      <div class="row"><span class="caps">Ingredients:</span><span class="head">Amount per serving % Daily Value</span></div>
      <div class="rule"></div>
      <div class="row"><span>Proprietary Formula</span><span>500mg</span></div>
      <div>Panax Notoginseng (Tienchi Ginseng root)</div>
      <div>Radix Salviae Miltiorrhizae, Ginkgo</div>
      <div class="foot">*Daily Value (DV) not established.</div>
    </div>
    <div class="band-bottom"><div class="dash dash--bottom"></div></div>
  </div>
</section>

<section class="label label--energy">
  <div class="panel panel--left">
    <div class="band-top"><div class="dash dash--top"></div></div>
    <p class="notes"><strong>Contains:</strong> All natural herbs and fibers. No sugar, salt, corn, soy, yeast, wheat, milk or preservatives.<br><strong>Caution:</strong><br>Pregnant women, children and anyone with disease should consult with their medical doctor prior to taking this product.<br><strong>Store in a cool, dry place below 30°C.</strong><br><strong>Avoid direct sunlight.</strong><br><strong>Keep out of reach of children.</strong><span class="fda">This statement has not been evaluated by the Food and Drug Administration. This product is not intended to diagnose, treat, cure or prevent any disease.</span><strong>Manufactured by:</strong><br>Ridgeway Herbal Labs Inc<br>Fairbrook, CA 90210</p>
    <div class="brand-side">Vel'dora</div>
    <div class="web">www.veldoranatural.com</div>
    <div class="band-bottom"><div class="dash dash--bottom"></div></div>
  </div>
  <div class="panel panel--center">
    <div class="band-top"></div>
    <div class="brand-top">Vel'dora</div>
    <h2 class="product-name">Vigor Renewal</h2>
    <p class="product-type">Dietary Supplement</p>
    <p class="count">60 Capsules</p>
    <div class="band-bottom"></div>
  </div>
  <div class="panel panel--right">
    <div class="band-top"><div class="dash dash--top"></div></div>
    <p class="usage"><strong>Suggested use:</strong><br>Take 2 to 3 capsules twice a day or as directed by healthcare professional.</p>
    <div class="facts">
      <h3>Supplement Facts</h3>
      <div class="rule"></div>
      <div>Serving Size: 2 Capsule</div>
      <div>Serving Per Container: 30</div>
      <div class="rule"></div>
      <div class="row"><span class="caps">Ingredients:</span><span class="head">Amount per serving % Daily Value</span></div>
      <div class="rule"></div>
      <div class="row"><span>Proprietary Formula</span><span>500mg</span></div>
      <div>Cistanche Tubulosa, Epimedium, Ginseng</div>
      <div class="foot">*Daily Value (DV) not established.</div>
    </div>
    <div class="band-bottom"><div class="dash dash--bottom"></div></div>
  </div>
</section>

<section class="label label--nose">
  <div class="panel panel--left">
    <div class="band-top"><div class="dash dash--top"></div></div>
    <p class="notes"><strong>Contains:</strong> All natural herbs and fibers. No sugar, salt, corn, soy, yeast, wheat, milk or preservatives.<br><strong>Caution:</strong><br>Pregnant women, children and anyone with disease should consult with their medical doctor prior to taking this product.<br><strong>Store in a cool, dry place below 30°C.</strong><br><strong>Avoid direct sunlight.</strong><br><strong>Keep out of reach of children.</strong><span class="fda">This statement has not been evaluated by the Food and Drug Administration. This product is not intended to diagnose, treat, cure or prevent any disease.</span><strong>Manufactured by:</strong><br>Ridgeway Herbal Labs Inc<br>Fairbrook, CA 90210</p>
    <div class="brand-side">Vel'dora</div>
    <div class="web">www.veldoranatural.com</div>
    <div class="band-bottom"><div class="dash dash--bottom"></div></div>
  </div>
  <div class="panel panel--center">
    <div class="band-top"></div>
    <div class="brand-top">Vel'dora</div>
    <h2 class="product-name">Clear Breath</h2>
    <p class="product-type">Dietary Supplement</p>
    <p class="count">90 Capsules</p>
    <div class="band-bottom"></div>
  </div>
  <div class="panel panel--right">
    <div class="band-top"><div class="dash dash--top"></div></div>
    <p class="usage"><strong>Suggested use:</strong><br>Take 3 capsules twice a day or as directed by healthcare professional.</p>
    <div class="facts">
      <h3>Supplement Facts</h3>
      <div class="rule"></div>
      <div>Serving Size: 2 Capsule</div>
      <div>Serving Per Container: 45</div>
      <div class="rule"></div>
      <div class="row"><span class="caps">Ingredients:</span><span class="head">Amount per serving % Daily Value</span></div>
      <div class="rule"></div>
      <div class="row"><span>Proprietary Formula</span><span>500mg</span></div>
      <div>Flos Magnoliae, Herba Houttuyniae, Radix Angelicae</div>
      <div>Dahuricae, Xanthium</div>
      <div class="foot">*Daily Value (DV) not established.</div>
    </div>
    <div class="band-bottom"><div class="dash dash--bottom"></div></div>
  </div>
</section>

</body>
</html>
```